Poster Design Project

Need a design for a music festival called Contra-Lindenfest

The design needs to have areas for the following:
- Band Names
- DJ Names
- Sponsor Names and Logos
- Event location, Date & Time

Industry/Entity Type

Festival

```html
<!DOCTYPE html>
<html lang="en">
<head>
<meta charset="utf-8">
<title>Contra-Lindenfest</title>
<link rel="stylesheet" href="https://fonts.googleapis.com/css2?family=Abril+Fatface&family=Bebas+Neue&family=Playfair+Display:ital,wght@1,900&display=swap">
<style>
  :root {
    --paper-light: #e2b374;
    --paper-mid: #cf9a58;
    --paper-dark: #a9773e;
    --ink: #111;
    --panel: #2b2620;
    --cream: #ecdfc8;
    --yellow: #f2d22e;
    --red: #d42a2c;
    --purple: #6b2d6b;
    --blue: #2a7498;
    --crimson: #b81e30;
    --brown: #a57e56;
    --green: #3ea572;
    --pink: #d23b72;
    --navy: #2c3a7a;
  }
  html, body { margin: 0; padding: 0; overflow: hidden; }
  .poster {
    position: relative;
    width: 848px; height: 1200px; overflow: hidden;
    background: radial-gradient(ellipse at 45% 40%, var(--paper-light) 0%, var(--paper-mid) 60%, var(--paper-dark) 100%);
    color: var(--ink);
  }
  .title {
    position: absolute; left: 0; top: 8px; width: 848px; margin: 0;
    text-align: center; font-family: "Abril Fatface", serif; font-weight: 400;
    font-size: 68px; letter-spacing: 3px; line-height: 1;
  }
  .rule { position: absolute; top: 113px; height: 2px; background: var(--ink); }
  .rule-left { left: 18px; width: 277px; }
  .rule-right { left: 548px; width: 282px; }
  .beneficiary {
    position: absolute; left: 300px; top: 88px; width: 248px;
    display: flex; align-items: center; justify-content: center; gap: 10px;
    font-family: "Bebas Neue", sans-serif; font-size: 38px; color: var(--navy); line-height: 1;
  }
  .beneficiary .mark { width: 22px; height: 22px; background: var(--navy); }
  .date {
    position: absolute; top: 176px; font-family: "Abril Fatface", serif;
    font-size: 42px; letter-spacing: 4px; line-height: 1;
  }
  .day { left: 18px; }
  .month { left: 388px; letter-spacing: 2px; }
  .day-num {
    position: absolute; left: 663px; top: 184px; width: 172px;
    font-family: "Abril Fatface", serif; font-size: 24px; line-height: 1;
    border-bottom: 2px solid var(--ink); padding-bottom: 4px; text-align: center;
  }
  .details {
    position: absolute; left: 0; width: 848px; margin: 0; text-align: center;
    font-family: "Playfair Display", serif; font-style: italic; font-weight: 900;
    font-size: 29px; letter-spacing: 2px; line-height: 1;
  }
  .address { top: 222px; padding-left: 40px; box-sizing: border-box; }
  .time { top: 256px; padding-right: 150px; box-sizing: border-box; }
  .lineup { position: absolute; left: 0; top: 0; }
  .band { font-family: "Bebas Neue", sans-serif; }
  .sponsors-label {
    position: absolute; left: 24px; top: 1064px;
    font-family: "Bebas Neue", sans-serif; font-size: 34px; color: var(--navy); letter-spacing: 1px;
  }
  .sponsor {
    position: absolute; display: flex; align-items: center; gap: 8px;
    font-family: "Bebas Neue", sans-serif; color: var(--ink); line-height: 1;
  }
  .sponsor .mark { width: 18px; height: 18px; background: var(--ink); flex: none; }
  .sponsor-crowd { left: 78px; top: 1112px; font-size: 46px; }
  .sponsor-eastside { left: 478px; top: 1108px; font-size: 30px; }
  .sponsor-larkfield { left: 712px; top: 1086px; width: 100px; font-size: 30px; color: var(--crimson); flex-wrap: wrap; text-align: center; justify-content: center; }
</style>
</head>
<body>
<main class="poster">
  <h1 class="title">CONTRA-LINDENFEST</h1>
  <div class="rule rule-left"></div>
  <div class="rule rule-right"></div>
  <div class="beneficiary"><span class="mark"></span><span>Cots for Youth</span></div>

  <div class="date day">SATURDAY</div>
  <div class="date month">September</div>
  <div class="day-num">15th, 2012</div>
  <p class="details address">512 W. 47th St Harlow, NC 28390</p>
  <p class="details time">11:00A - Until</p>

  <svg class="lineup" width="848" height="1200" viewBox="0 0 848 1200" aria-label="Band lineup">
    <rect x="24" y="303" width="801" height="755" fill="var(--panel)"/>
    <rect x="278" y="348" width="284" height="172" fill="var(--red)"/>
    <ellipse cx="188" cy="435" rx="145" ry="117" fill="var(--yellow)"/>
    <ellipse cx="665" cy="470" rx="153" ry="140" fill="var(--purple)"/>
    <rect x="46" y="535" width="459" height="172" fill="var(--blue)"/>
    <rect x="458" y="647" width="348" height="118" fill="var(--crimson)"/>
    <ellipse cx="200" cy="845" rx="168" ry="152" fill="var(--brown)"/>
    <rect x="146" y="963" width="439" height="90" fill="var(--pink)"/>
    <ellipse cx="612" cy="880" rx="194" ry="170" fill="var(--green)"/>

    <g fill="var(--cream)">
      <polygon points="46,314 49,322 57,322 51,327 53,335 46,330 39,335 41,327 35,322 43,322"/>
      <polygon points="782,322 785,330 793,330 787,335 789,343 782,338 775,343 777,335 771,330 779,330"/>
      <polygon points="510,533 513,541 521,541 515,546 517,554 510,549 503,554 505,546 499,541 507,541"/>
      <polygon points="660,622 663,630 671,630 665,635 667,643 660,638 653,643 655,635 649,630 657,630"/>
      <polygon points="390,730 393,738 401,738 395,743 397,751 390,746 383,751 385,743 379,738 387,738"/>
      <polygon points="436,866 439,874 447,874 441,879 443,887 436,882 429,887 431,879 425,874 433,874"/>
      <polygon points="108,932 111,940 119,940 113,945 115,953 108,948 101,953 103,945 97,940 105,940"/>
      <polygon points="776,1012 779,1020 787,1020 781,1025 783,1033 776,1028 769,1033 771,1025 765,1020 773,1020"/>
    </g>

    <g class="band" text-anchor="middle">
      <g transform="rotate(-5 200 440)" fill="var(--ink)" font-size="60">
        <text x="215" y="432">QUIET</text>
        <text x="195" y="492">BOROUGH</text>
      </g>
      <text x="446" y="428" fill="var(--cream)" font-size="64">ODD</text>
      <text x="440" y="496" fill="var(--cream)" font-size="64">THEORY</text>
      <text x="680" y="468" fill="var(--ink)" font-size="60">CLARA</text>
      <text x="680" y="540" fill="var(--ink)" font-size="60">WHITFIELD</text>
      <text x="275" y="612" fill="var(--cream)" font-size="62">ROWE &amp;</text>
      <text x="272" y="685" fill="var(--cream)" font-size="58">TANNER COMPANY</text>
      <text x="632" y="738" fill="var(--ink)" font-size="64">THE MEASURED</text>
      <text x="200" y="825" fill="var(--cream)" font-size="66">MOTH</text>
      <text x="200" y="895" fill="var(--cream)" font-size="66">LANTERN</text>
      <text x="765" y="870" fill="var(--cream)" font-size="66" text-anchor="end">THE</text>
      <text x="620" y="940" fill="var(--cream)" font-size="66">GREYWOLVES</text>
      <text x="334" y="1037" fill="var(--ink)" font-size="64">GROOVY CODGER</text>
    </g>
  </svg>

  <div class="sponsors-label">SPONSORS:</div>
  <div class="sponsor sponsor-crowd"><span class="mark"></span><span>MoveTheCrowd.net</span></div>
  <div class="sponsor sponsor-eastside"><span class="mark"></span><span>Eastside Brewing Co</span></div>
  <div class="sponsor sponsor-larkfield"><span>Larkfield Brewing</span></div>
</main>
</body>
</html>
```